Electrical company business card design.

Hi, were an electrical company in kerrowvale New Zealand called Quarneth Ltd. We focus mainly on high end residential and commercial so the card would be targeted towards that.
The card will be for myself, i am the director of the company.
Name: Derek Olstow
Position: Director/electrician
Phone: 021 387 9415
Email: derek@quarneth.co.nz
Location: kerrowvale
As for colors the the blue color in the logo is preferred, i also don't mind a black background option.
Target Market(s)
High end residential and commercial
Industry/Entity Type
Electrician
Contact Information for Business Card
Name: Derek Olstow Position: Director/Electrician Phone: 021 387 9415, Email: derek@quarneth.co.nz, Location: kerrowvale

```html
<!DOCTYPE html>
<html lang="en">
<head>
<meta charset="utf-8">
<title>Quarneth Ltd — Business Card</title>
<link rel="stylesheet" href="https://fonts.googleapis.com/css2?family=Open+Sans:wght@400;600;700&display=swap">
<style>
  :root {
    --stage: #e9eaec;
    --card: #ffffff;
    --pattern-light: #ffffff;
    --pattern-tint: #f1f3f8;
    --brand-blue: #1f5fb5;
    --ink: #4a4b4d;
    --ink-soft: #6d6e70;
  }
  * { margin: 0; padding: 0; box-sizing: border-box; }
  html, body {
    width: 1200px; height: 1200px; overflow: hidden;
    background: var(--stage);
    font-family: "Open Sans", Arial, sans-serif;
  }
  .canvas { position: relative; width: 1200px; height: 1200px; }

  .card {
    position: absolute; left: 200px; width: 800px; height: 458px;
    background: var(--card); overflow: hidden;
  }
  .card--front { top: 86px; }
  .card--back { top: 651px; }

  .card__pattern {
    position: absolute; inset: 0;
    background: linear-gradient(160deg, var(--pattern-light) 0%, var(--pattern-tint) 55%, var(--pattern-light) 100%);
  }

  /* Front */
  .front-brand {
    position: absolute; left: 160px; top: 222px;
    display: flex; align-items: center; gap: 12px;
    font-size: 32px; font-weight: 700; color: var(--brand-blue);
  }
  .front-brand__mark { width: 16px; height: 16px; background: var(--brand-blue); }
  .divider {
    position: absolute; left: 395px; top: 173px;
    width: 2px; height: 133px; background: var(--brand-blue);
  }
  .contact { position: absolute; left: 448px; top: 166px; }
  .contact__name { font-size: 34px; line-height: 1.1; color: var(--ink); font-weight: 400; }
  .contact__first { color: var(--brand-blue); }
  .contact__role { font-size: 15px; color: var(--ink-soft); margin-top: 2px; margin-bottom: 8px; }
  .contact__list { list-style: none; }
  .contact__item {
    display: flex; align-items: center; gap: 12px;
    font-size: 17px; line-height: 24px; color: var(--ink);
  }
  .contact__icon { width: 13px; height: 13px; fill: var(--brand-blue); flex: none; }

  /* Back */
  .back-lockup {
    position: absolute; left: 0; right: 0; top: 172px;
    display: flex; flex-direction: column; align-items: center;
  }
  .back-brand {
    display: flex; align-items: center; gap: 18px;
    font-size: 62px; font-weight: 700; color: var(--ink); letter-spacing: 2px;
    line-height: 1;
  }
  .back-brand__mark { width: 30px; height: 30px; border-radius: 50%; background: var(--brand-blue); }
  .tagline {
    margin-top: 14px; margin-left: 48px;
    font-size: 21px; font-weight: 700; color: var(--brand-blue); letter-spacing: 1px;
  }
</style>
</head>
<body>
<main class="canvas">

  <section class="card card--front" aria-label="Business card front">
    <div class="card__pattern" role="img" aria-label="Faint repeating brand-mark pattern across the card"></div>
    <div class="front-brand"><span class="front-brand__mark"></span>Quarneth</div>
    <div class="divider"></div>
    <div class="contact">
      <h1 class="contact__name"><span class="contact__first">Derek</span> Olstow</h1>
      <p class="contact__role">Director</p>
      <ul class="contact__list">
        <li class="contact__item">
          <svg class="contact__icon" viewBox="0 0 24 24" aria-hidden="true"><path d="M6.6 10.8a15.1 15.1 0 0 0 6.6 6.6l2.2-2.2a1 1 0 0 1 1-.25 11.4 11.4 0 0 0 3.6.57 1 1 0 0 1 1 1V20a1 1 0 0 1-1 1A17 17 0 0 1 3 4a1 1 0 0 1 1-1h3.5a1 1 0 0 1 1 1c0 1.25.2 2.45.57 3.57a1 1 0 0 1-.25 1z"/></svg>
          021 387 9415
        </li>
        <li class="contact__item">
          <svg class="contact__icon" viewBox="0 0 24 24" aria-hidden="true"><path d="M2 5h20v14H2z"/></svg>
          derek@quarneth.co.nz
        </li>
        <li class="contact__item">
          <svg class="contact__icon" viewBox="0 0 24 24" aria-hidden="true"><path d="M12 2a7 7 0 0 0-7 7c0 5.25 7 13 7 13s7-7.75 7-13a7 7 0 0 0-7-7zm0 9.5A2.5 2.5 0 1 1 12 6.5a2.5 2.5 0 0 1 0 5z"/></svg>
          kerrowvale
        </li>
      </ul>
    </div>
  </section>

  <section class="card card--back" aria-label="Business card back">
    <div class="card__pattern" role="img" aria-label="Faint repeating brand-mark pattern across the card"></div>
    <div class="back-lockup">
      <div class="back-brand"><span class="back-brand__mark"></span>QUARNETH</div>
      <p class="tagline">WIRED FOR EXCELLENCE</p>
    </div>
  </section>

</main>
</body>
</html>
```